RuneHollow.com - Layered PSD Photoshop

Hey everyone,
I am moving my blog from PostLoom to Pagecraft, so I figured I would also re-design the look at the same time. The old blog is at www.runehollow.com. The website is on Sorcery: the Assembly, a collectible card game. Every weekday, I post up one or two articles by my writers who talk about the strategy of the game. The main page should show 5 articles.
We need a layered PSD that I will find someone later to convert to a Pagecraft theme. As for the current banner of the site, that can be ignored as I look towards a completely fresh start. The PSD of our old logo can be found here: http://qpx-northgate.com/images/Rune%20H%20Logo.psd.
-UPDATE- New logo being designed right now.
We are about to sign a contract with http://www.tablewisehobby.com/ who will be our exclusive sponsor going forward. There should be some sign that Rune Hollow is "Powered by Tablewise Hobby Shop". Feel free to use their logo.
As for the actual design, go crazy. I feel all the current major sites (brightlanecards.com, deckforgehub.com, cardvaultly.com) try to do too much. I just want something simple, but a whole lot sleeker than what I currently have. Do not try to copy what I currently have.
If price needs to be increased for this job, feel free to let me know.
After checking some designs for other contests, I think I want buttons with icons for the top menu. Top menu should be: Home / Store / Articles / Videos / Podcasts / Events.
New Logo: http://runehollow.com/2011/01/a-new-rune-h-a-new-logo.html
Target Market(s)
14-32 males, mostly
Industry/Entity Type
Store
Requirements
Must have
- One thing the blog should keep from the old one is the icy-blue feel. I like that. A section called "This Week on Rune H" which lists the articles published during the week. People should be able to easily follow me on Chirpline.
Should not have
- One of the more famous blogs on Sorcery: the Assembly is Deckforge Hub (http://www.deckforgehub.com/category/home/). I want to make a note that I feel that website has way too much going and would not want something like that. I also do not want one of those "rotating panels". www.murkyledger.com that also uses that and I do not like the look. It is pretty but not useful.

```html
<!DOCTYPE html>
<html lang="en">
<head>
<meta charset="utf-8">
<title>Rune Hollow</title>
<link rel="stylesheet" href="https://fonts.googleapis.com/css2?family=IM+Fell+English:ital@0;1&family=Lora:ital,wght@0,400;0,700;1,400&display=swap">
<style>
:root{
  --night:#04101f;
  --deep:#0a2444;
  --panel:#0c2340;
  --panel-edge:#2a4a72;
  --glow:#3f7fd6;
  --gold:#d8a92c;
  --gold-soft:#c9a640;
  --ink:#e8eef6;
  --cyan:#52c7d9;
  --violet:#9b8fe0;
  --parchment:#cfc6ae;
  --parchment-dark:#8f8670;
  --sponsor:#d8642a;
}
*{box-sizing:border-box;margin:0;padding:0}
html,body{width:1200px;height:900px;overflow:hidden}
body{
  position:relative;
  font-family:"Lora",Georgia,serif;
  color:var(--ink);
  background:
    radial-gradient(ellipse 260px 180px at 600px 170px, rgba(70,130,220,.35), transparent 70%),
    radial-gradient(ellipse 520px 520px at 600px 420px, #0d2b52, transparent 75%),
    repeating-linear-gradient(90deg, rgba(255,255,255,.015) 0 2px, transparent 2px 7px),
    var(--night);
}
a{color:inherit;text-decoration:none}

/* header */
.brand{position:absolute;left:383px;top:60px;font-family:"IM Fell English",Georgia,serif;font-size:27px;color:#aab7c6;letter-spacing:.5px}
.brand-mark{position:absolute;left:432px;top:6px;width:52px;height:52px;border-radius:50%;background:#3a5068}
.hero-figure{position:absolute;left:540px;top:0;width:150px;height:140px;
  background:radial-gradient(ellipse 60px 80px at 50% 45%, #2c6b86, #16345a 60%, transparent 100%);}
.hero-flame{position:absolute;left:370px;top:90px;width:480px;height:150px;
  background:radial-gradient(ellipse 240px 50px at 50% 40%, rgba(80,150,240,.45), transparent 75%);}
.social{position:absolute;left:684px;top:6px;display:flex;gap:8px;font-size:9px}
.social a{display:flex;align-items:center;gap:3px;color:#cfe0f2}
.social i{display:block;width:10px;height:10px;border-radius:2px;background:#5b8fd0}

/* nav */
.main-nav{position:absolute;left:386px;top:124px;width:430px;height:26px;
  background:linear-gradient(180deg,var(--parchment),var(--parchment-dark));
  transform:rotate(.6deg);border-radius:2px;display:flex;align-items:center;justify-content:space-around;padding:0 14px;
  box-shadow:0 0 12px rgba(90,150,230,.5)}
.main-nav a{font-family:"IM Fell English",Georgia,serif;font-style:italic;font-size:14px;color:#2b2a26;display:flex;align-items:center;gap:3px}
.main-nav i{width:13px;height:13px;border-radius:50%;display:block;border:1px solid #333}
.ic-home{background:#8a8a8a}.ic-store{background:#e9e4d2}.ic-articles{background:#2f6fb0}
.ic-videos{background:#bfbfbf}.ic-podcasts{background:#c8322a}.ic-events{background:#3a8f3a}

/* page panel */
.page{position:absolute;left:397px;top:148px;width:413px;height:692px;
  background:linear-gradient(180deg,rgba(14,38,70,.92),rgba(10,28,52,.95));
  border:1px solid var(--panel-edge);border-top:none;border-radius:0 0 26px 26px}
.page::after{content:"";position:absolute;left:270px;top:0;bottom:40px;width:1px;background:rgba(90,130,180,.4)}

/* posts */
.post{position:absolute;left:25px;width:236px}
.post + .post::before{content:"";position:absolute;left:-4px;right:-6px;top:-10px;height:1px;background:rgba(90,130,180,.35)}
.post-head{position:relative;height:40px}
.post-mark{position:absolute;left:4px;top:12px;width:24px;height:20px;border-radius:50%;background:#5c6c80}
.post-title{position:absolute;left:34px;top:7px;font-size:11.5px;font-style:italic;font-weight:400;color:var(--gold)}
.post-date{position:absolute;left:34px;top:24px;font-size:5.6px;font-style:italic;color:var(--gold-soft)}
.post-count{position:absolute;left:176px;top:-2px;width:36px;height:38px}
.post-count span{position:absolute;left:0;right:0;top:15px;text-align:center;font-size:13px;color:#fff}
.post-body{font-size:6.9px;line-height:8px;color:var(--ink)}
.post-art{float:left;width:130px;height:47px;margin:1px 6px 2px 2px;border:2px solid #f4f1e4;
  background:linear-gradient(180deg,#c6bf8a,#6e7d52 55%,#b6a970)}
.post-more{display:block;clear:both;margin:6px 0 0 3px;font-size:6.9px;color:var(--cyan);text-decoration:underline}
.post-meta{margin:4px 0 0 4px;font-size:6.9px;color:var(--ink)}
.post-meta a{color:var(--violet)}

/* sidebar */
.sidebar{position:absolute;left:683px;top:0;width:130px}
.widget{position:absolute;left:0;width:130px}
.widget h2{font-size:11px;font-style:italic;font-weight:400;color:var(--gold);margin-bottom:6px}
.widget li{list-style:none;font-size:7.6px;line-height:13px;padding-left:6px}
.search-box{display:flex;gap:6px;align-items:center}
.search-box span{display:block;width:86px;height:13px;border-radius:4px;background:#2a3f5c;border:1px solid #5a7396;font-size:6px;padding:2px 5px;color:#dfe8f3}
.search-box b{display:block;width:15px;height:13px;border-radius:4px;background:#1b2a3e;border:1px solid #6d83a3;font-size:5.5px;text-align:center;line-height:11px}
.tweets{padding-left:6px;font-size:5.6px;line-height:6.4px;width:122px}
.tweets p{margin-bottom:0}
.tweets a{color:var(--cyan)}
.tweets em{font-style:normal;color:var(--gold)}

/* footer */
.copyright{position:absolute;left:412px;top:845px;font-size:7.8px}
.powered{position:absolute;left:757px;top:845px;font-size:7.8px}
.sponsor{position:absolute;left:689px;top:857px;width:110px;height:29px;background:var(--sponsor);border:1px solid #6a3a1a;
  font-size:8px;color:#fff;display:flex;align-items:center;justify-content:center}
</style>
</head>
<body>

<header>
  <div class="hero-flame" role="img" aria-label="Swirling blue arcane flames behind the menu"></div>
  <div class="brand-mark"></div>
  <div class="brand">Rune Hollow</div>
  <div class="hero-figure" role="img" aria-label="Hooded mage wreathed in blue flame"></div>
  <nav class="social">
    <a href="#"><i></i>RSS</a>
    <a href="#"><i></i>Chirpline</a>
    <a href="#"><i></i>Friendwall</a>
  </nav>
  <nav class="main-nav">
    <a href="#"><i class="ic-home"></i>Home</a>
    <a href="#"><i class="ic-store"></i>Store</a>
    <a href="#"><i class="ic-articles"></i>Articles</a>
    <a href="#"><i class="ic-videos"></i>Videos</a>
    <a href="#"><i class="ic-podcasts"></i>Podcasts</a>
    <a href="#"><i class="ic-events"></i>Events</a>
  </nav>
</header>

<main class="page">
  <article class="post" style="top:12px">
    <div class="post-head">
      <div class="post-mark"></div>
      <h1 class="post-title">Lorem ipsum dolor sit amet</h1>
      <div class="post-date">Thursday , December 16 , 2010</div>
      <div class="post-count"><svg width="36" height="38" viewBox="0 0 36 38"><path d="M18 2 C24 10 34 16 32 26 C30 34 24 37 18 37 C10 37 4 33 4 26 C4 16 14 10 18 2Z" fill="#2f69b8" opacity=".85"/></svg><span>18</span></div>
    </div>
    <div class="post-body">
      <div class="post-art" role="img" aria-label="Card set banner artwork"></div>
      Lorem ipsum dolor sit amet, consectetur adipiscing elit. Nullam vitae ligula et diam rutrum dignissim at sed elit. Etiam vehicula elit ac felis mollis suscipit. Nullam sed justo nec diam pulvinar eleifend. Nam eros sapien, feugiat ut molestie a, elementum quis massa. Pellentesque eu magna vitae massa auctor vestibulum. Praesent id odio at libero hendrerit gravida ac in risus. Phasellus nunc erat, tincidunt in auctor sit amet, accumsan non leo. Nulla viverra ultrices sagittis. Integer feugiat pretium sem, a viverra lacus eleifend vel. Sed sed risus sed massa adipiscing interdum. Donec id nunc eget ipsum ...
      <a class="post-more" href="#">Continue Reading "Lorem Ipsum Dolor Sit Amet"</a>
      <div class="post-meta">Posted at 12:55 AM in <a href="#">Vestibulum porta</a> | <a href="#">Permalink</a> | <a href="#">Comments (18)</a></div>
    </div>
  </article>

  <article class="post" style="top:190px">
    <div class="post-head">
      <div class="post-mark"></div>
      <h1 class="post-title">Lorem ipsum dolor sit amet</h1>
      <div class="post-date">Thursday , December 16 , 2010</div>
      <div class="post-count"><svg width="36" height="38" viewBox="0 0 36 38"><path d="M18 2 C24 10 34 16 32 26 C30 34 24 37 18 37 C10 37 4 33 4 26 C4 16 14 10 18 2Z" fill="#2f69b8" opacity=".85"/></svg><span>67</span></div>
    </div>
    <div class="post-body">
      <div class="post-art" role="img" aria-label="Card set banner artwork"></div>
      Lorem ipsum dolor sit amet, consectetur adipiscing elit. Nullam vitae ligula et diam rutrum dignissim at sed elit. Etiam vehicula elit ac felis mollis suscipit. Nullam sed justo nec diam pulvinar eleifend. Nam eros sapien, feugiat ut molestie a, elementum quis massa. Pellentesque eu magna vitae massa auctor vestibulum. Praesent id odio at libero hendrerit gravida ac in risus. Phasellus nunc erat, tincidunt in auctor sit amet, accumsan non leo. Nulla viverra ultrices sagittis. Integer feugiat pretium sem, a viverra lacus eleifend vel. Sed sed risus sed massa adipiscing interdum. Donec id nunc eget ipsum ...
      <a class="post-more" href="#">Continue Reading "Lorem Ipsum Dolor Sit Amet"</a>
      <div class="post-meta">Posted at 12:55 AM in <a href="#">Vestibulum porta</a> | <a href="#">Permalink</a> | <a href="#">Comments (18)</a></div>
    </div>
  </article>

  <article class="post" style="top:370px">
    <div class="post-head">
      <div class="post-mark"></div>
      <h1 class="post-title">Lorem ipsum dolor sit amet</h1>
      <div class="post-date">Thursday , December 16 , 2010</div>
      <div class="post-count"><svg width="36" height="38" viewBox="0 0 36 38"><path d="M18 2 C24 10 34 16 32 26 C30 34 24 37 18 37 C10 37 4 33 4 26 C4 16 14 10 18 2Z" fill="#2f69b8" opacity=".85"/></svg><span>25</span></div>
    </div>
    <div class="post-body">
      <div class="post-art" role="img" aria-label="Card set banner artwork" style="border-color:#222"></div>
      Lorem ipsum dolor sit amet, consectetur adipiscing elit. Nullam vitae ligula et diam rutrum dignissim at sed elit. Etiam vehicula elit ac felis mollis suscipit. Nullam sed justo nec diam pulvinar eleifend. Nam eros sapien, feugiat ut molestie a, elementum quis massa. Pellentesque eu magna vitae massa auctor vestibulum. Praesent id odio at libero hendrerit gravida ac in risus. Phasellus nunc erat, tincidunt in auctor sit amet, accumsan non leo. Nulla viverra ultrices sagittis. Integer feugiat pretium sem, a viverra lacus eleifend vel. Sed sed risus sed massa adipiscing interdum. Donec id nunc eget ipsum ...
      <a class="post-more" href="#">Continue Reading "Lorem Ipsum Dolor Sit Amet"</a>
      <div class="post-meta">Posted at 12:55 AM in <a href="#">Vestibulum porta</a> | <a href="#">Permalink</a> | <a href="#">Comments (25)</a></div>
    </div>
  </article>
</main>

<aside class="sidebar">
  <section class="widget" style="top:165px">
    <h2>Search</h2>
    <div class="search-box"><span>Looking for something ?</span><b>GO!</b></div>
  </section>
  <section class="widget" style="top:207px">
    <h2>About</h2>
    <ul><li>About Rune Hollow</li><li>The Team</li><li>Contact</li><li>Write for Us</li></ul>
  </section>
  <section class="widget" style="top:286px">
    <h2>This week on Rune H</h2>
    <ul><li>Lorem ipsum</li><li>Dolor sit amet</li><li>Consectetur adipiscing elit</li><li>Nullam vitae</li></ul>
  </section>
  <section class="widget" style="top:374px">
    <h2>Categories</h2>
    <ul><li>Vestibulum porta</li><li>Aenean ullamcorper sem</li><li>Nam tristique velit</li><li>Praesent et arcu</li><li>Quisque fermentum</li></ul>
  </section>
  <section class="widget" style="top:475px">
    <h2>Chirpline Updates</h2>
    <div class="tweets">
      <p><a href="#">@stormwright</a> But it's SO BAD. Zero interaction save for a cheap trap? <em>12 minutes ago</em></p>
      <p><a href="#">@stormwright</a> I have the cards, time for you to lose to the mythic build. <em>22 minutes ago</em></p>
      <p>Logged onto an old account of mine and found out I actually have four rare spells and four reflecting wells. WHAT?! <em>23 minutes ago</em></p>
      <p><a href="#">@tidecaller</a> <a href="#">@ashgrove_3</a> <a href="#">@deckhollow</a> Neglecting positional needs, in a typical keeper league, Sifter or Markstone? <em>about 2 hours ago</em></p>
      <p><a href="#">@glasswarden</a> I believe Ben Harlow experimented with that against me. He had Relic Adept. This was before Nationals. <em>about 4 hours ago</em></p>
    </div>
  </section>
  <section class="widget" style="top:627px">
    <h2>SoA Stores</h2>
    <ul><li>Tablewise Hobby Shop</li></ul>
  </section>
  <section class="widget" style="top:667px">
    <h2>SoA Blogs</h2>
    <ul><li>Sixty Slots</li><li>The Shattered Town Spellcraft School</li></ul>
  </section>
</aside>

<footer>
  <p class="copyright">Copyright © Rune Hollow</p>
  <p class="powered">Powered by</p>
  <a class="sponsor" href="#">Tablewise Hobby Shop</a>
</footer>

</body>
</html>
```